New Company Logo & Responsive Website Design for Codeweave Orchard

Codeweave Orchard provides a white labeled, digital lending platform technology solutions to the mortgage industry via a SaaS model. Our target market is Mortgage Companies and Banks who are looking for innovative technology to assist both borrowers and loan originators with the lending process, while automating as much of he process as possible.

Codeweave Orchard is our company name, and our modular software offerings Include the following Products:

1) Applicant Orchard: A customizable, web based, point-of-sale application for borrowers to complete a loan application, and guide them through the mortgage process.

POS Definition
"A point of sale (POS) is the client-facing software solution that allows borrowers to create a customer portal, apply for a loan online, and seamlessly submit needed documentation."

2) Escrowmap Orchard: A Mortgage Loan Origination System

LOS Definition
"A Mortgage Loan Origination System (LOS) is a platform that takes a completed loan application and facilitates the mortgage transaction from origination to post closing. LOS systems may include document management, pricing and eligibility engines, and compliance tools to decrease risk and increase loan manufacturing quality.

3) Dwelling Orchard: A brandable, home search website

The LOS and POS definitions provided above are just for your understanding of what these products are, not to be included word-for-word as website content.

We are looking for designs that are elegant, convey technical competency, simple to navigate, and set us apart from the competition.

We are not set on any particular colors at this point, so feel free to choose the best colors for your particular designs.

Please include company logo, both desktop and mobile designs with a template design for the website sub pages.

Some Examples of Mortgage Technology Websites offering similar products. These are to show the typical content, not designs that we particularly like or dislike.

https://trenvask.com/
https://www.brightquorel.com/
https://www.dwelfundbuddy.com/
https://www.escrowotter.com/
https://www.quennidata.com/products/route

Please send comments with additional questions.

Thank You For your participation.

```html
<!DOCTYPE html>
<html lang="en">
<head>
<meta charset="utf-8">
<title>Codeweave Orchard — Mortgage Software</title>
<link href="https://fonts.googleapis.com/css2?family=Poppins:wght@300;400;500;600&display=swap" rel="stylesheet">
<style>
:root{
  --purple:#6a4cf0;
  --purple-deep:#5a3fe6;
  --violet:#8a6cf6;
  --navy:#1f2a6b;
  --ink:#1a1a1a;
  --muted:#6f6f7a;
  --line:#e8e8f0;
  --soft:#f6f6f9;
  --blue:#1a8cf0;
  --amber:#e9a61f;
  --star:#f2c400;
  --black:#0b0b0c;
  --white:#ffffff;
}
*{margin:0;padding:0;box-sizing:border-box}
html,body{width:1200px;height:4386px;overflow:hidden}
body{font-family:'Poppins',sans-serif;color:var(--ink);position:relative;background:var(--white)}
.abs{position:absolute}
.bg-svg{position:absolute;left:0;top:0}
.brand{font-weight:600;color:var(--white);font-size:25px;white-space:nowrap}
.nav a{color:var(--white);font-size:14px;text-decoration:none;position:absolute;top:28px}
.pill{position:absolute;border-radius:8px;font-size:13px;display:flex;align-items:center;justify-content:center}
.pill.white{background:var(--white);color:var(--purple)}
.pill.purple{background:linear-gradient(90deg,#8a4ff0,#6a3fe6);color:var(--white)}
.hero-title{left:60px;top:138px;color:var(--white);font-size:44px;line-height:56px;font-weight:400}
.hero-text{left:60px;top:312px;width:450px;color:var(--white);font-size:13px;line-height:23px}
.sec-title{left:0;width:1200px;text-align:center;font-size:31px;font-weight:500}
.sec-text{left:320px;width:560px;text-align:center;font-size:13px;line-height:22px;color:var(--muted)}
.logo-row{position:absolute;left:60px;top:862px;width:1080px;display:flex;justify-content:space-between;align-items:center;height:40px}
.logo-row span{font-size:21px;color:#5a5a62;font-weight:400;white-space:nowrap}
.card{position:absolute;background:var(--white);border-radius:6px;box-shadow:0 6px 24px rgba(40,40,90,.08);text-align:center}
.badge{position:absolute;width:54px;height:54px;border-radius:50%;color:var(--white);font-size:15px;display:flex;align-items:center;justify-content:center;border-bottom-right-radius:0}
.card .ico{width:64px;height:64px;border-radius:50%;background:#eef0fb;margin:22px auto 0;display:flex;align-items:center;justify-content:center}
.card h3{font-size:16px;font-weight:500;line-height:24px;margin-top:22px}
.card p{font-size:12.5px;line-height:22px;color:var(--muted);margin-top:10px}
.prod-title{font-size:30px;font-weight:500}
.prod-text{font-size:13px;line-height:22.5px}
.prod-text p+p{margin-top:10px}
.mock{position:absolute;background:var(--soft);border-radius:10px;box-shadow:0 6px 24px rgba(40,40,90,.1);overflow:hidden}
.mock .bar{height:50px;background:var(--white);position:relative}
.dots{position:absolute;left:24px;top:20px;display:flex;gap:5px}
.dots i{width:7px;height:7px;border-radius:50%;background:#555;display:block}
.field{height:20px;background:#f1f1f5;border-radius:2px;font-size:8px;color:#888;padding-left:8px;line-height:20px;margin-top:9px}
.stat{position:absolute;top:2519px;width:199px;height:136px;background:var(--white);border-radius:6px;box-shadow:0 4px 16px rgba(30,30,80,.12)}
.stat .lab{position:absolute;left:58px;top:38px;font-size:12.5px}
.stat .val{position:absolute;left:24px;top:72px;font-size:16px}
.stat .sub{position:absolute;left:24px;top:100px;font-size:9px}
.stat svg{position:absolute;left:20px;top:24px}
.white-txt{color:var(--white)}
.foot-h{font-size:13px;color:var(--purple);position:absolute;top:4131px}
.foot-l{font-size:12px;color:var(--white);position:absolute}
</style>
</head>
<body>

<svg class="bg-svg" width="1200" height="4386" viewBox="0 0 1200 4386" aria-hidden="true">
  <defs>
    <linearGradient id="heroGrad" x1="0" y1="0" x2="1" y2="1">
      <stop offset="0" stop-color="#8a63f5"/><stop offset="1" stop-color="#5b44ea"/>
    </linearGradient>
    <linearGradient id="bandGrad" x1="0" y1="0" x2="0" y2="1">
      <stop offset="0" stop-color="#6a4cf0"/><stop offset="1" stop-color="#5c45ea"/>
    </linearGradient>
  </defs>
  <path d="M0 0H1200V420C1060 560 860 660 620 645C380 630 200 520 0 500Z" fill="url(#heroGrad)"/>
  <path d="M0 1070C240 980 960 980 1200 1070V1430C960 1530 240 1530 0 1430Z" fill="#f7f7fa"/>
  <path d="M0 2330C300 2210 700 2230 1200 2300V3300C900 3420 500 3300 0 3420Z" fill="url(#bandGrad)"/>
  <path d="M0 2860C300 2780 650 2900 1200 2820V3300C900 3420 500 3300 0 3420Z" fill="#6448ee"/>
  <path d="M0 3990C300 4040 900 4040 1200 3960V4386H0Z" fill="var(--black)"/>
</svg>

<!-- header -->
<div class="abs brand" style="left:60px;top:16px">Codeweave Orchard</div>
<nav class="nav">
  <a style="left:420px">Products</a><a style="left:512px">Solutions</a>
  <a style="left:607px">Resources</a><a style="left:711px">Company</a>
  <a style="left:922px">Log In</a>
</nav>
<div class="pill white" style="left:992px;top:22px;width:148px;height:34px">Request A Demo</div>

<!-- hero -->
<h1 class="abs hero-title">Mortgage Software &amp;<br>digital technology<br>Solutions</h1>
<p class="abs hero-text">Lorem Ipsum is simply dummy text of the printing and typesetting industry. Lorem Ipsum has been the industry's</p>
<div class="pill white" style="left:60px;top:397px;width:136px;height:34px">Start Free Trial</div>
<div class="abs" role="img" aria-label="Laptop showing a loan calculator dashboard" style="left:690px;top:330px;width:500px;height:260px;background:linear-gradient(150deg,#ffffff,#dcdcea);border-radius:20px;transform:skewY(-20deg);transform-origin:left top;opacity:.95"></div>
<div class="abs" role="img" aria-label="Phone showing a monthly payment calculator" style="left:510px;top:400px;width:170px;height:250px;background:linear-gradient(160deg,#ffffff,#e4e0fb);border-radius:24px;transform:rotate(-28deg);box-shadow:0 10px 30px rgba(40,20,120,.25)"></div>

<!-- trusted -->
<h2 class="abs sec-title" style="top:734px">Trusted By 15000+ Loan Officers</h2>
<p class="abs sec-text" style="top:781px">Lorem Ipsum is simply dummy text of the printing and typesetting industry. Lorem Ipsum has been the industry's standard dummy text</p>
<div class="logo-row">
  <span>Veridane</span>
  <span>Halcrest Lending</span>
  <span>Orbelle</span>
  <span>Quillmark</span>
  <span>Pinecove Bank</span>
  <span>Tarnwick</span>
</div>

<!-- benefits -->
<h2 class="abs sec-title" style="top:1038px">Our Benefits</h2>
<p class="abs sec-text" style="top:1086px">Lorem Ipsum is simply dummy text of the printing and typesetting industry. Lorem Ipsum has been the industry's standard dummy text</p>

<div class="card" style="left:87px;top:1180px;width:311px;height:222px">
  <div class="ico"><svg width="34" height="34" viewBox="0 0 34 34" fill="none" stroke="#333" stroke-width="1.5"><circle cx="17" cy="12" r="8"/><circle cx="17" cy="10" r="3"/><path d="M11 17c2-3 10-3 12 0M8 30l2-4 2 4M15 30l2-4 2 4M22 30l2-4 2 4"/></svg></div>
  <h3>Deliver A Modern<br>Borrower Experience</h3>
  <p>Lorem Ipsum is simply dummy text<br>of the printing.</p>
</div>
<div class="badge" style="left:60px;top:1158px;background:var(--blue)">#1</div>

<div class="card" style="left:465px;top:1180px;width:311px;height:222px">
  <div class="ico"><svg width="34" height="34" viewBox="0 0 34 34" fill="none" stroke="#333" stroke-width="1.5"><rect x="5" y="6" width="24" height="16" rx="1"/><path d="M13 28h8M17 22v6"/><rect x="16" y="10" width="9" height="8" stroke="#6a4cf0"/><path d="M9 11h4M9 15h4"/></svg></div>
  <h3>Increase Borrower<br>Conversions</h3>
  <p>Lorem Ipsum is simply dummy text<br>of the printing.</p>
</div>
<div class="badge" style="left:438px;top:1158px;background:var(--purple-deep)">#1</div>

<div class="card" style="left:829px;top:1180px;width:311px;height:222px">
  <div class="ico"><svg width="34" height="34" viewBox="0 0 34 34" fill="none" stroke="#333" stroke-width="1.5"><rect x="6" y="5" width="14" height="5"/><rect x="8" y="10" width="14" height="5"/><rect x="6" y="15" width="14" height="5"/><circle cx="23" cy="23" r="7" stroke="#6a4cf0"/><path d="M23 19v8"/></svg></div>
  <h3>Improve Efficiency<br>and Decrease Costs</h3>
  <p>Lorem Ipsum is simply dummy text<br>of the printing.</p>
</div>
<div class="badge" style="left:802px;top:1158px;background:var(--amber)">#1</div>

<!-- products -->
<h2 class="abs sec-title" style="top:1606px">Our Products</h2>
<p class="abs sec-text" style="top:1653px">Lorem Ipsum is simply dummy text of the printing and typesetting industry. Lorem Ipsum has been the industry's standard dummy text</p>

<h3 class="abs prod-title" style="left:61px;top:1780px;color:var(--navy)">Applicant Orchard</h3>
<div class="abs prod-text" style="left:61px;top:1827px;width:430px;color:#555">
  <p>Lorem Ipsum is simply dummy text of the printing and typesetting industry. Lorem Ipsum has been the industry's standard dummy text ever since the 1500s, when an unknown printer took a galley of type and scrambled it to make a type specimen book.</p>
  <p>It has survived not only five centuries, but also the leap into electronic typesetting, remaining essentially unchanged.</p>
</div>
<div class="pill purple" style="left:61px;top:2039px;width:111px;height:37px;border-radius:18px 18px 18px 4px">Read More</div>

<div class="mock" style="left:567px;top:1724px;width:573px;height:412px">
  <div class="bar"><div class="dots"><i></i><i></i><i></i></div>
    <div class="pill purple" style="left:482px;top:14px;width:58px;height:24px;font-size:10px;border-radius:12px">Login</div></div>
  <div class="abs" style="left:40px;top:135px;font-size:13px;font-weight:500">Your Industry Exports</div>
  <div class="abs" style="left:40px;top:158px;width:250px;font-size:9.5px;line-height:18px;color:var(--muted)">Mortgage Demo Is Your Online Resources For a Stress-Free process and amazing Service</div>
  <div class="abs" role="img" aria-label="Portrait of a loan consultant" style="left:36px;top:214px;width:56px;height:56px;border-radius:50%;background:linear-gradient(160deg,#3b5b8a,#c9d4e6)"></div>
  <div class="abs" style="left:117px;top:226px;font-size:12px;font-weight:500">Daniel Reeve</div>
  <div class="abs" style="left:117px;top:252px;font-size:9.5px;color:var(--muted)">Loan Consult</div>
  <div class="abs" style="left:117px;top:276px;font-size:9.5px;color:var(--muted)"><span style="color:var(--amber)">✆</span>&nbsp; NMLS#1234567</div>
  <div class="abs" style="left:117px;top:302px;font-size:9.5px;color:var(--muted)"><span style="color:var(--amber)">✉</span>&nbsp; 123 456 7890</div>
  <div class="abs" style="left:303px;top:97px;width:250px;height:278px;background:var(--white);border-radius:6px;padding:20px 20px">
    <div style="font-size:15px;font-weight:500;line-height:21px">Let's get started on your loan application!</div>
    <div class="field" style="margin-top:14px">First Name*</div><div class="field">Last Name*</div>
    <div class="field">E-mail*</div><div class="field">Phone*</div><div class="field">Password*</div>
    <div class="pill purple" style="position:relative;margin-top:14px;width:104px;height:26px;font-size:10px;border-radius:13px">Get Started</div>
  </div>
</div>

<!-- escrowmap -->
<div class="abs" style="left:60px;top:2357px;width:570px;height:409px;background:var(--soft);border-radius:10px;box-shadow:0 8px 30px rgba(20,10,80,.3)">
  <div style="height:50px;background:var(--white);border-radius:10px 10px 0 0;position:relative"><div class="dots"><i></i><i></i><i></i></div></div>
  <div class="abs" role="img" aria-label="Profile photo of a user" style="left:26px;top:80px;width:58px;height:58px;border-radius:50%;background:linear-gradient(160deg,#2f4f7a,#c6d0e2)"></div>
  <div class="abs" style="left:100px;top:94px;font-size:14px;font-weight:500">My Dashboard</div>
  <div class="abs" style="left:100px;top:120px;width:154px;height:4px;background:#e2e2ea;border-radius:2px"></div>
  <div class="abs" style="left:26px;top:328px;font-size:14px;font-weight:500">Today's Rates</div>
  <div class="abs" style="left:26px;top:357px;width:176px;height:4px;background:#e2e2ea"></div>
  <div class="abs" style="left:240px;top:357px;width:66px;height:4px;background:#e2e2ea"></div>
  <div class="abs" style="left:357px;top:357px;width:66px;height:4px;background:#e2e2ea"></div>
  <div class="abs" style="left:472px;top:357px;width:46px;height:4px;background:#e2e2ea"></div>
</div>
<div class="stat" style="left:31px"><svg width="30" height="30" viewBox="0 0 30 30" fill="none" stroke="#333" stroke-width="1.3"><rect x="3" y="5" width="18" height="22" rx="2"/><circle cx="19" cy="19" r="7" stroke="#6a4cf0"/><path d="M7 11h8M7 15h5"/></svg><div class="lab">Loan Amount</div><div class="val">$460,000</div></div>
<div class="stat" style="left:247px"><svg width="30" height="30" viewBox="0 0 30 30" fill="none" stroke="#333" stroke-width="1.3"><path d="M3 14L15 4l12 10M6 12v14h18V12"/><path d="M11 22l8-8" stroke="#6a4cf0"/><circle cx="12" cy="15" r="1.5"/><circle cx="18" cy="21" r="1.5"/></svg><div class="lab">Featured Rate</div><div class="val">5.125%</div><div class="sub">Rate/APR</div></div>
<div class="stat" style="left:456px"><svg width="30" height="30" viewBox="0 0 30 30" fill="none" stroke="#333" stroke-width="1.3"><rect x="4" y="5" width="22" height="22" rx="2"/><path d="M8 17a7 7 0 0 1 14 0" stroke="#6a4cf0"/><path d="M15 17l3-4"/></svg><div class="lab">Credit Score</div><div class="val">740</div><div class="sub">Estimated</div></div>

<h3 class="abs prod-title white-txt" style="left:715px;top:2410px">Escrowmap Orchard</h3>
<div class="abs prod-text white-txt" style="left:715px;top:2459px;width:420px">
  <p>Lorem Ipsum is simply dummy text of the printing and typesetting industry. Lorem Ipsum has been the industry's standard dummy text ever since the 1500s, when an unknown printer took a galley of type and scrambled it to make a type specimen book.</p>
  <p>It has survived not only five centuries, but also the leap into electronic typesetting, remaining essentially unchanged.</p>
</div>
<div class="pill white" style="left:715px;top:2672px;width:111px;height:34px;border-radius:17px 17px 17px 4px">Read More</div>

<!-- dwelling -->
<h3 class="abs prod-title white-txt" style="left:61px;top:2956px">Dwelling Orchard</h3>
<div class="abs prod-text white-txt" style="left:61px;top:3003px;width:430px">
  <p>Lorem Ipsum is simply dummy text of the printing and typesetting industry. Lorem Ipsum has been the industry's standard dummy text ever since the 1500s, when an unknown printer took a galley of type and scrambled it to make a type specimen book.</p>
  <p>It has survived not only five centuries, but also the leap into electronic typesetting, remaining essentially unchanged.</p>
</div>
<div class="pill white" style="left:61px;top:3217px;width:111px;height:37px;border-radius:18px 18px 18px 4px">Read More</div>

<svg class="abs" style="left:730px;top:2960px" width="360" height="380" viewBox="730 2960 360 380" aria-label="Partner badges">
  <g fill="#8f7bf5"><circle cx="892" cy="2986" r="4"/><circle cx="830" cy="3077" r="4"/><circle cx="1038" cy="3094" r="4"/><circle cx="936" cy="3133" r="4"/><circle cx="880" cy="3242" r="4"/><circle cx="823" cy="3326" r="4"/><circle cx="965" cy="3298" r="4"/><circle cx="1010" cy="3225" r="3"/></g>
  <g fill="#ffffff">
    <circle cx="781" cy="3014" r="27"/><circle cx="979" cy="3021" r="43"/><circle cx="904" cy="3082" r="20"/>
    <circle cx="834" cy="3164" r="36"/><circle cx="1052" cy="3174" r="26"/><circle cx="955" cy="3206" r="22"/>
    <circle cx="771" cy="3251" r="26"/><circle cx="1023" cy="3276" r="31"/><circle cx="888" cy="3292" r="22"/>
  </g>
  <g fill="#3b6fb8" opacity=".8">
    <rect x="772" y="3006" width="18" height="16"/><rect x="962" y="3008" width="34" height="26"/><rect x="896" y="3075" width="16" height="14"/>
    <rect x="818" y="3148" width="32" height="32"/><rect x="1042" y="3164" width="20" height="20"/><rect x="946" y="3197" width="18" height="18"/>
    <rect x="761" y="3241" width="20" height="20"/><rect x="1011" y="3264" width="24" height="24"/><rect x="879" y="3283" width="18" height="18"/>
  </g>
</svg>

<!-- testimonials -->
<h2 class="abs sec-title" style="top:3431px">Testimonials</h2>
<p class="abs sec-text" style="top:3479px">Lorem Ipsum is simply dummy text of the printing and typesetting industry. Lorem Ipsum has been the industry's standard dummy text</p>
<div class="abs" role="img" aria-label="Portrait of a smiling client in a suit" style="left:203px;top:3549px;width:269px;height:269px;border-radius:134px 134px 0 134px;background:linear-gradient(170deg,#e9ecf1,#c6ccd6 55%,#2a3550)"></div>
<div class="abs" style="left:529px;top:3560px;color:var(--star);font-size:17px;letter-spacing:5px">★★★★★</div>
<p class="abs" style="left:529px;top:3591px;width:510px;font-size:13px;line-height:23px;color:#555">Lorem Ipsum is simply dummy text of the printing and typesetting industry. Lorem Ipsum has been the industry's standard dummy text ever since the 1500s, when an unknown printer took a galley of type and scrambled it to make a type specimen book. It has survived not only five centuries, but also the leap into electronic typesetting.</p>
<div class="abs" style="left:529px;top:3717px;font-size:13px">Client Name</div>
<div class="abs" style="left:529px;top:3742px;font-size:12.5px;color:var(--purple)">C.E.O Codeweave Orchard</div>
<svg class="abs" style="left:529px;top:3777px" width="140" height="32" viewBox="0 0 140 32" aria-hidden="true">
  <rect x="0" y="0" width="60" height="32" rx="16" fill="#fff" stroke="#eee"/>
  <path d="M42 16H18M24 10l-6 6 6 6" stroke="#111" stroke-width="2" fill="none"/>
  <path d="M80 16h24M98 10l6 6-6 6" stroke="#6a4cf0" stroke-width="2" fill="none"/>
</svg>

<!-- cta -->
<div class="abs" style="left:60px;top:3906px;width:1080px;height:170px;background:linear-gradient(90deg,#5b44ea,#5a46e8);border-radius:8px"></div>
<h2 class="abs white-txt" style="left:115px;top:3945px;font-size:30px;font-weight:500">Ready To See More</h2>
<p class="abs white-txt" style="left:115px;top:3993px;width:560px;font-size:13px;line-height:22px">Lorem Ipsum is simply dummy text of the printing and typesetting industry. Lorem Ipsum has been the industry's standard dummy text</p>
<div class="pill white" style="left:894px;top:3972px;width:151px;height:35px;border-radius:18px 18px 18px 4px">Request A Demo</div>

<!-- footer -->
<div class="abs brand" style="left:61px;top:4120px;font-size:23px">Codeweave Orchard</div>
<svg class="abs" style="left:60px;top:4182px" width="20" height="110" viewBox="0 0 20 110" fill="none" stroke="#6a4cf0" stroke-width="1.5" aria-hidden="true">
  <path d="M10 2a6 6 0 0 1 6 6c0 5-6 11-6 11S4 13 4 8a6 6 0 0 1 6-6z"/><circle cx="10" cy="8" r="2"/>
  <path d="M4 52c2-3 4-3 5-1l-2 3c1 3 3 5 6 6l3-2c2 1 2 3-1 5-6 2-13-6-11-11z"/>
  <rect x="2" y="88" width="16" height="11" rx="1"/><path d="M2 89l8 6 8-6"/>
</svg>
<div class="foot-l" style="left:91px;top:4180px;width:220px;line-height:20px">Lorem Ipsum is simply dummy text of the.</div>
<div class="foot-l" style="left:91px;top:4231px">123-456-7890</div>
<div class="foot-l" style="left:91px;top:4268px">info@codeweaveorchard.com</div>

<div class="foot-h" style="left:336px">Quick Links</div>
<div class="foot-l" style="left:337px;top:4162px">Products</div>
<div class="foot-l" style="left:337px;top:4193px">Solutions</div>
<div class="foot-l" style="left:337px;top:4223px">Resources</div>
<div class="foot-l" style="left:337px;top:4257px">Company</div>

<div class="foot-h" style="left:614px">Products</div>
<div class="foot-l" style="left:614px;top:4162px">Applicant Orchard</div>
<div class="foot-l" style="left:614px;top:4193px">Escrowmap Orchard</div>
<div class="foot-l" style="left:614px;top:4223px">Dwelling Orchard</div>

<div class="foot-h" style="left:890px">Company</div>
<div class="foot-l" style="left:891px;top:4162px">About</div>
<div class="foot-l" style="left:891px;top:4193px">Careers</div>
<div class="foot-l" style="left:891px;top:4223px">FAQs</div>

<div class="abs" style="left:0;top:4342px;width:1200px;text-align:center;color:var(--white);font-size:11px">© 2022 Codeweave Orchard. All Rights Reserved.</div>

</body>
</html>
```